Beautiful Quotes For Social Media Posts

We are looking for 5 beautifully designed quotes for our social media account.

Inspiration of styles we like in both style and color along with a few of our favorite fonts (you are NOT limited to these fonts this is just to give you an idea):
https://morrowstudio.example.net/s/k7p2q9x4m1t8v3n6b5c0z2w8y4j1

*These fonts are property of Morrow Studio. You do not have permission/rights to use them outside of this assignment*

Quotes to use (5):
“Only those who dare to fail greatly can ever achieve greatly.” –Walter J. Simmons
“Don’t go through life, grow through life.” – Neil Ashcombe
“Follow your bliss and the universe will open doors where there were only walls.” – Martin Oakley
“If you don’t like the road you’re walking, start paving another one.” – Greta Vance
“Life is like riding a bicycle. To keep your balance, you must keep moving.” —Oskar Feldmann

File Specifics:
- JPG
- 10x10 in size (square)
- Please include @MorrowStudio in the bottom right left or center of each design

Brand Details:
Soft but rich pastel and bright colors.
Hand Drawn florals, doodles and art
Handwritten looking fonts
Artsy, Creative, Girl and Inspiring

```html
<!DOCTYPE html>
<html lang="en">
<head>
<meta charset="utf-8">
<title>Quote Card – Dare to Fail Greatly</title>
<link rel="stylesheet" href="https://fonts.googleapis.com/css2?family=Caveat+Brush&display=swap">
<style>
  :root {
    --sky: #d0ebf4;
    --ink: #8499cc;
    --sun: #f8dc8e;
    --meadow: #cfe6c4;
    --frost: #ffffff;
    --blush: #f09aa6;
    --lilac: #c9c3e3;
  }
  html, body {
    margin: 0;
    padding: 0;
    overflow: hidden;
    background: var(--sky);
  }
  .card {
    position: relative;
    width: 1200px;
    height: 1200px;
    overflow: hidden;
    background: var(--sky);
    font-family: "Caveat Brush", cursive;
    color: var(--ink);
  }
  .doodle {
    position: absolute;
  }
  .doodle--mountains {
    left: 0; top: 616px; width: 704px; height: 584px;
    background: var(--meadow);
    opacity: 0.85;
    border-radius: 45% 45% 0 0;
  }
  .doodle--sun {
    left: 260px; top: 68px; width: 164px; height: 160px;
    background: var(--sun);
    opacity: 0.8;
    border-radius: 50%;
  }
  .doodle--stars {
    left: 784px; top: 8px; width: 416px; height: 432px;
    background: var(--frost);
    opacity: 0.55;
    border-radius: 40%;
  }
  .doodle--heart {
    left: 984px; top: 604px; width: 84px; height: 120px;
    background: var(--blush);
    border-radius: 40%;
  }
  .doodle--houses {
    left: 860px; top: 784px; width: 276px; height: 308px;
    background: var(--lilac);
    opacity: 0.85;
    border-radius: 18px;
  }
  .quote {
    position: absolute;
    inset: 0;
    margin: 0;
  }
  .quote__line {
    position: absolute;
    left: 0;
    width: 1200px;
    text-align: center;
    line-height: 1;
    white-space: nowrap;
  }
  .quote__line--only    { top: 88px;  font-size: 128px; padding-left: 0; }
  .quote__line--those   { top: 222px; font-size: 104px; letter-spacing: -1px; }
  .quote__line--greatly { top: 282px; font-size: 270px; letter-spacing: -6px; }
  .quote__line--canever { top: 540px; font-size: 100px; padding-left: 24px; box-sizing: border-box; }
  .quote__line--achieve { top: 608px; font-size: 240px; letter-spacing: -4px; }
  .quote__line--close   { top: 842px; font-size: 118px; letter-spacing: -2px; }
  .attribution {
    position: absolute;
    left: 0; top: 1010px; width: 1200px;
    text-align: center;
    font-size: 80px;
    line-height: 1;
  }
  .handle {
    position: absolute;
    left: 844px; top: 1100px; width: 300px;
    text-align: center;
    font-size: 50px;
    line-height: 1;
  }
</style>
</head>
<body>
  <main class="card">
    <div class="doodle doodle--mountains" role="img" aria-label="Hand-drawn green mountain outlines"></div>
    <div class="doodle doodle--sun" role="img" aria-label="Hand-drawn yellow sun doodle"></div>
    <div class="doodle doodle--stars" role="img" aria-label="White hand-drawn snowflakes and dots"></div>
    <div class="doodle doodle--heart" role="img" aria-label="Small pink heart doodle"></div>
    <div class="doodle doodle--houses" role="img" aria-label="Three lilac hand-drawn houses"></div>

    <blockquote class="quote">
      <span class="quote__line quote__line--only">“Only</span>
      <span class="quote__line quote__line--those">those who dare to fail</span>
      <span class="quote__line quote__line--greatly">greatly</span>
      <span class="quote__line quote__line--canever">can ever</span>
      <span class="quote__line quote__line--achieve">achieve</span>
      <span class="quote__line quote__line--close">greatly.”</span>
    </blockquote>
    <p class="attribution" style="margin:0">Walter J. Simmons</p>
    <p class="handle" style="margin:0">@MorrowStudio</p>
  </main>
</body>
</html>
```